Bref créative
The Lanternwrights
Clear paths, steady light
Professional
Rosalind Kettering
Partner
48 Thornapple Lane
Marbury Falls, OR 97382
rosalind.k.kettering@thelanternwrights.net
www.thelanternwrights.net
logo will be attached
second set of business cards needed
Dean Oltveld
dean.oltveld@thelanternwrights.net
Your Trusted Advisors
Updated logo in CMYK format

```html
<!DOCTYPE html>
<html lang="en">
<head>
<meta charset="UTF-8">
<title>The Lanternwrights – Business Cards</title>
<link rel="stylesheet" href="https://fonts.googleapis.com/css2?family=Archivo+Black&family=Arimo:wght@400;700&display=swap">
<style>
  :root {
    --page: #ffffff;
    --brand-red: #e8271a;
    --brand-orange: #f4581c;
    --orange-light: #ff7a2e;
    --orange-deep: #e0360f;
    --blue-light: #3d7bff;
    --blue-deep: #1633c9;
    --accent-blue: #2b5fd9;
    --ink: #1c1c1c;
    --ink-soft: #444444;
    --white: #ffffff;
  }
  * { box-sizing: border-box; margin: 0; padding: 0; }
  html, body { width: 1200px; height: 787px; overflow: hidden; background: var(--page); }
  body { position: relative; font-family: "Arimo", Arial, sans-serif; }

  .card {
    position: absolute;
    width: 520px;
    height: 297px;
    border-radius: 14px;
    overflow: hidden;
    box-shadow: 0 6px 18px rgba(0,0,0,0.18);
  }
  .card--front { left: 50px; top: 70px; background: var(--white); border: 1px solid #dddddd; }
  .card--orange { left: 630px; top: 70px; background: radial-gradient(circle at 50% 45%, var(--orange-light), var(--orange-deep) 80%); }
  .card--blue { left: 340px; top: 420px; background: radial-gradient(circle at 50% 45%, var(--blue-light), var(--blue-deep) 85%); }

  .front-top-band {
    position: absolute; left: 0; top: 0; width: 100%; height: 14px;
    background: linear-gradient(90deg, var(--brand-red), var(--brand-orange));
  }
  .front-corner { position: absolute; top: 0; width: 40px; height: 22px; }
  .front-corner--left { left: 0; }
  .front-corner--right { right: 0; }

  .brand {
    position: absolute; left: 0; right: 0;
    display: flex; flex-direction: column; align-items: center;
  }
  .card--front .brand { top: 38px; }
  .card--orange .brand, .card--blue .brand { top: 82px; }

  .brand-mark {
    width: 62px; height: 62px; border-radius: 50%;
    background: var(--brand-red);
    margin-bottom: 8px;
  }
  .card--orange .brand-mark { background: var(--blue-deep); }
  .card--blue .brand-mark { background: var(--brand-red); }

  .brand-name {
    font-family: "Archivo Black", Arial, sans-serif;
    font-size: 24px; letter-spacing: 0.5px; line-height: 1;
    color: var(--ink);
  }
  .brand-tagline {
    margin-top: 4px;
    font-family: "Archivo Black", Arial, sans-serif;
    font-size: 9px; letter-spacing: 1px;
    color: var(--brand-red);
  }
  .card--orange .brand-tagline { color: var(--blue-deep); }

  .contact {
    position: absolute; left: 20px; top: 196px;
    font-size: 9.5px; line-height: 1.55; color: var(--ink-soft);
  }
  .contact-label { color: var(--brand-red); font-weight: 700; margin-right: 4px; }

  .person {
    position: absolute; right: 24px; top: 204px; text-align: center;
  }
  .person-name { font-weight: 700; font-size: 13px; color: var(--brand-orange); }
  .person-title { font-size: 8.5px; color: var(--ink-soft); margin-top: 3px; }

  .front-bottom-band {
    position: absolute; left: 0; bottom: 0; width: 100%; height: 26px;
    background: linear-gradient(90deg, var(--brand-red), var(--brand-orange));
    clip-path: polygon(34% 0, 100% 0, 100% 100%, 0 100%, 0 60%, 30% 60%);
  }
  .front-web {
    position: absolute; right: 24px; bottom: 6px;
    font-size: 10.5px; color: var(--white); letter-spacing: 0.3px;
  }
</style>
</head>
<body>

  <section class="card card--front" aria-label="Business card front">
    <div class="front-top-band"></div>
    <svg class="front-corner front-corner--left" viewBox="0 0 40 22"><polygon points="0,0 30,0 0,22" fill="var(--accent-blue)"/></svg>
    <svg class="front-corner front-corner--right" viewBox="0 0 40 22"><polygon points="40,0 10,0 40,22" fill="var(--accent-blue)"/></svg>

    <div class="brand">
      <div class="brand-mark"></div>
      <div class="brand-name">THE LANTERNWRIGHTS</div>
      <div class="brand-tagline">CLEAR PATHS, STEADY LIGHT</div>
    </div>

    <div class="contact">
      <div>48 Thornapple Lane Marbury Falls, OR 97382</div>
      <div><span class="contact-label">E :</span>rosalind.k.kettering@thelanternwrights.net</div>
      <div><span class="contact-label">C :</span>215-555-0148</div>
    </div>

    <div class="person">
      <div class="person-name">Rosalind Kettering</div>
      <div class="person-title">Partner</div>
    </div>

    <div class="front-bottom-band"></div>
    <div class="front-web">www.thelanternwrights.net</div>
  </section>

  <section class="card card--orange" aria-label="Business card back, orange">
    <div class="brand">
      <div class="brand-mark"></div>
      <div class="brand-name">THE LANTERNWRIGHTS</div>
      <div class="brand-tagline">CLEAR PATHS, STEADY LIGHT</div>
    </div>
  </section>

  <section class="card card--blue" aria-label="Business card back, blue">
    <div class="brand">
      <div class="brand-mark"></div>
      <div class="brand-name">THE LANTERNWRIGHTS</div>
      <div class="brand-tagline">CLEAR PATHS, STEADY LIGHT</div>
    </div>
  </section>

</body>
</html>
```